Business Card Design

We are a florist shop that also stocks a range of giftware and jewellery. I would like a new design that incorporates a light green background. If you could use a skeleton leaf somewhere in the design that would be great. I would also like to incorporate the find us on Friendlink logo on this design.

Industry/Entity Type

Florist

Contact Information for Business Card

Petals on Larkmore
41 Brindle street
Denhollow Victoria 3871
Phone: 0352983047
Fax : 0352983066
email: pol@wrenmail.net.au

Proprietors : Dana & Lee Thornwick

```html
<!DOCTYPE html>
<html lang="en">
<head>
<meta charset="utf-8">
<title>Petals on Larkmore — Business Card</title>
<link href="https://fonts.googleapis.com/css2?family=Dancing+Script:wght@600&family=PT+Sans&display=swap" rel="stylesheet">
<style>
  :root {
    --backdrop: #4a4a4a;
    --card-top: #b9dc8d;
    --card-mid: #eaf4dd;
    --card-white: #ffffff;
    --brand-green: #137a3e;
    --wave-dark: #007a3a;
    --wave-main: #009a49;
    --wave-bright: #12ae4b;
    --wave-lime: #6dbf45;
    --stripe-lime: #8dc63f;
    --ornament: #c8e2a0;
    --ink: #111111;
    --on-green: #ffffff;
  }
  * { margin: 0; padding: 0; box-sizing: border-box; }
  html, body { width: 1200px; height: 999px; overflow: hidden; }
  body { background: var(--backdrop); position: relative; font-family: "PT Sans", sans-serif; }

  .business-card {
    position: absolute; left: 68px; top: 192px;
    width: 1064px; height: 614px; overflow: hidden;
    background: linear-gradient(to bottom, var(--card-top) 0%, var(--card-mid) 32%, var(--card-white) 52%, var(--card-white) 100%);
  }
  .card-art { position: absolute; inset: 0; }

  .shop-name {
    position: absolute; left: 0; right: 0; top: 68px;
    text-align: center;
    font-family: "Dancing Script", cursive; font-weight: 600;
    font-size: 108px; line-height: 1; color: var(--brand-green);
  }
  .proprietors {
    position: absolute; left: 312px; top: 274px;
    font-size: 44px; color: var(--ink);
  }
  .shop-address {
    position: absolute; left: 712px; top: 405px;
    font-size: 28px; line-height: 37.5px; color: var(--ink);
    font-style: normal; white-space: nowrap;
  }
  .contact-list {
    position: absolute; left: 68px; top: 480px;
    list-style: none; color: var(--on-green);
    font-size: 27px; line-height: 37.5px;
  }
  .contact-list li { display: flex; align-items: center; }
  .contact-icon { width: 24px; height: 24px; margin-right: 40px; fill: var(--on-green); flex: none; }
</style>
</head>
<body>
  <section class="business-card">
    <svg class="card-art" viewBox="0 0 1064 614" width="1064" height="614">
      <defs>
        <radialGradient id="ornament-glow" cx="0.55" cy="0.55" r="0.55">
          <stop offset="0" stop-color="var(--ornament)" stop-opacity="0.75"/>
          <stop offset="1" stop-color="var(--ornament)" stop-opacity="0"/>
        </radialGradient>
        <linearGradient id="wave-fill" x1="0" y1="0" x2="1" y2="0">
          <stop offset="0" stop-color="var(--wave-dark)"/>
          <stop offset="0.5" stop-color="var(--wave-main)"/>
          <stop offset="0.75" stop-color="var(--wave-bright)"/>
          <stop offset="1" stop-color="var(--wave-lime)"/>
        </linearGradient>
      </defs>
      <ellipse class="floral-swirl" role="img" aria-label="Pale green floral swirl with curling vines and leaves"
               cx="640" cy="390" rx="270" ry="190" fill="url(#ornament-glow)"/>
      <path class="wave-band" fill="var(--wave-dark)"
            d="M0 440 C120 395 260 400 420 450 C600 505 760 560 880 540 C960 528 1020 510 1064 500 L1064 614 L0 614 Z"/>
      <path class="wave-stripe" fill="var(--stripe-lime)"
            d="M0 452 C120 410 260 415 420 463 C600 518 760 572 880 552 C960 540 1020 522 1064 512 L1064 520 C1020 530 960 548 880 560 C760 580 600 526 420 471 C260 423 120 418 0 460 Z"/>
      <path class="wave-body" fill="url(#wave-fill)"
            d="M0 466 C120 426 260 430 420 478 C600 533 760 586 880 566 C960 554 1020 538 1064 528 L1064 614 L0 614 Z"/>
    </svg>

    <h1 class="shop-name">Petals On Larkmore</h1>
    <p class="proprietors">Dana &amp; Lee Thornwick</p>

    <address class="shop-address">
      Petals on Larkmore<br>
      41 Brindle street<br>
      Denhollow Victoria 3871
    </address>

    <ul class="contact-list">
      <li>
        <svg class="contact-icon" viewBox="0 0 24 24" aria-label="Phone"><path d="M6.6 10.8a15 15 0 0 0 6.6 6.6l2.2-2.2a1 1 0 0 1 1-.25 11.4 11.4 0 0 0 3.6.57 1 1 0 0 1 1 1V20a1 1 0 0 1-1 1A17 17 0 0 1 3 4a1 1 0 0 1 1-1h3.5a1 1 0 0 1 1 1c0 1.25.2 2.45.57 3.6a1 1 0 0 1-.25 1z"/></svg>
        0352983047
      </li>
      <li>
        <svg class="contact-icon" viewBox="0 0 24 24" aria-label="Fax"><path d="M6 2h9l3 3v6H6z M3 12h18v10H3z M7 15h3v2H7z M12 15h3v2h-3z M7 18h3v2H7z M12 18h3v2h-3z"/></svg>
        0352983066
      </li>
      <li>
        <svg class="contact-icon" viewBox="0 0 24 24" aria-label="Email"><path d="M2 8l10-6 10 6v13H2z M4 9l8 5 8-5-8-5z"/></svg>
        pol@wrenmail.net.au
      </li>
    </ul>
  </section>
</body>
</html>
```